Swimming Pool Service business card needed!!!! Please

Hi Everyone! Thanks for looking at my contest. I PROMISE to provide excellent feedback during this process.

I am starting a new swimming pool cleaning business in San Diego, California and would like your help in making a business card for me.

I like easy to read, classy and sophisticated.

I am having a website designed and I'm looking for it to have pictures of really clean & clear pools.

I really like the blue on white color format, but open to other colors.

I do not have a logo, but the name of my company is GLIMMERTIDE POOL SERVICE.

My tag line is: Pools so clean, you can see yourself "in" them. (does not need to have the quotes around "in"...maybe just italics for this word IN?) You decide for me.

I would like to have a logo designed that incorporates some sort of easy to read letters. I do not want cursive (handwriting) letters. I thought about having a "reflection" of letters (mirror image), but think that this will be hard to read from far away. Maybe you can surprise me and come up with an idea that works using the a mirror image....but I'm not sure. I was leaning toward plain old BLOCK letters as I think it would be easy to read on my truck.

I would like to have the NAQTR and WBK logos on the back of the card. I have attached those two as files. You can put other things on the back as well, but I need these two logos on there. Or maybe put them on the front of the card if you have a better idea for the back of the card! :-)

Maybe blue on the back of the card and white on the front of the card? I don't know, I'm just thinking out loud.

I had another card done awhile ago called HARBORLINE TEES. I have uploaded a copy of that card for your reference. I don't want this card to be the same as my new company is a swimming pool cleaning company, but I wanted you to see what I liked in the past.

THANK YOU!!!!
Updates

Reason: Partner out of town and want their feedback....so need more time to decide and designs still coming in.

Industry/Entity Type

Business

Contact Information for Business Card

GLIMMERTIDE POOL SERVICE
Dale Wexby
Owner
4817 Quarry Bend Ave. #512
San Diego, CA 92417
858-291-6083
www.glimmertidepoolservice.example

Font styles to use
Sans Serif

Colors
0255a3
3176b5
ffffff

Requirements
Nice to have
• Some things to (possibly) add to back of card (in no particular order)
• WBK logo
• NAQTR logo
• Free Estimates
• Residential and Commercial Services
• Equipment Repairs
• Saltwater Systems
• Licensed, Bonded, Insured
• Family Owned and Operated
• No Contracts
• =======================
• Check out the FolioMint business card that i attached.
• i think they did this using a chrome overlay.
• Can any of you guys design that? or is that done at my printer?
• ==================
Should not have
• Hi Designers-
• The first round of cards came back and let's stay away from the light blue (powder blue) color. I don't like the look of it on the business cards.
• Also, the pool company JPG's that I attached are other logos of pool companies that I liked. I don't want them to be on my card. The only logos that should be on my card are the one you are going to come up with for my company, the WBK logo and the NAQTR logo.
• Lastly, no vertical cards and no split cards (logo on left, contact info on right side).
• Thanks much!

```html
<!DOCTYPE html>
<html lang="en">
<head>
<meta charset="utf-8">
<title>Glimmertide Pool Service – Business Card</title>
<link rel="stylesheet" href="https://fonts.googleapis.com/css2?family=Dosis:wght@800&family=Questrial&family=Share+Tech&display=swap">
<style>
  :root {
    --page: #ffffff;
    --aqua: #6cb3df;
    --ocean: #3176b5;
    --deep-ink: #0255a3;
    --name-plate: #5d9fd3;
    --edge-tone: #4f90c8;
    --swim-icon: #0a8fcc;
    --slate: #7fa5d0;
    --stripe: #0694d0;
    --title-blue: #0a7fc4;
    --contact-ink: #0255a3;
  }
  html, body {
    margin: 0;
    padding: 0;
    width: 1200px;
    height: 1000px;
    overflow: hidden;
    background: var(--page);
  }
  .sheet { display: block; width: 1200px; height: 1000px; }
  .front-top { fill: var(--aqua); }
  .front-band { fill: var(--ocean); }
  .edge-pattern { fill: var(--edge-tone); }
  .swim-mark { fill: var(--swim-icon); }
  .name-plate { fill: var(--name-plate); }
  .front-name {
    font-family: "Dosis", sans-serif;
    font-weight: 800;
    font-size: 44px;
    fill: var(--deep-ink);
  }
  .back-field { fill: var(--slate); }
  .back-stripe { fill: var(--stripe); }
  .contact-panel { fill: var(--aqua); }
  .title-plate { fill: var(--aqua); }
  .back-title {
    font-family: "Questrial", sans-serif;
    font-size: 45px;
    fill: var(--title-blue);
  }
  .contact-line {
    font-family: "Share Tech", sans-serif;
    font-variant: small-caps;
    font-size: 21px;
    letter-spacing: 2.4px;
    fill: var(--contact-ink);
  }
  .contact-web {
    font-family: "Share Tech", sans-serif;
    font-variant: small-caps;
    font-size: 16px;
    letter-spacing: 1.4px;
    fill: var(--contact-ink);
  }
</style>
</head>
<body>
<svg class="sheet" viewBox="0 0 1200 1000" xmlns="http://www.w3.org/2000/svg">
  <defs>
    <linearGradient id="steps-fill" x1="0" y1="1" x2="1" y2="0">
      <stop offset="0" stop-color="#6cb3df"/>
      <stop offset="1" stop-color="#7fa5d0"/>
    </linearGradient>
  </defs>

  <!-- Front of card -->
  <g class="card-front">
    <rect class="front-top" x="180" y="9" width="840" height="247"/>
    <rect class="front-band" x="180" y="256" width="840" height="247"/>

    <rect class="edge-pattern" x="180" y="9" width="90" height="494"
          role="img" aria-label="Staggered column of dots along the left edge"/>
    <rect class="edge-pattern" x="931" y="9" width="89" height="494"
          role="img" aria-label="Staggered column of dots along the right edge"/>

    <rect class="swim-mark" x="463" y="98" width="247" height="152" rx="6"
          role="img" aria-label="Swimmer pictogram above wavy water lines"/>

    <rect class="name-plate" x="347" y="332" width="486" height="82"/>
    <text class="front-name" x="590" y="390" text-anchor="middle" textLength="470" lengthAdjust="spacingAndGlyphs">GLIMMERTIDE POOL SERVICE</text>
  </g>

  <!-- Back of card -->
  <g class="card-back">
    <rect class="back-field" x="182" y="512" width="838" height="478"/>
    <rect class="back-stripe" x="805" y="512" width="50" height="478"/>
    <rect class="back-stripe" x="891" y="512" width="50" height="478"/>
    <rect class="back-stripe" x="972" y="512" width="48" height="478"/>

    <rect class="contact-panel" x="182" y="805" width="406" height="185"/>
    <rect x="537" y="608" width="264" height="247" fill="url(#steps-fill)"
          role="img" aria-label="Stepped pool stairs rising toward the stripes"/>

    <rect class="title-plate" x="232" y="600" width="289" height="73"/>
    <text class="back-title" x="244" y="655" textLength="404" lengthAdjust="spacingAndGlyphs">GLIMMERTIDE POOL</text>
    <text class="back-title" x="370" y="716" textLength="165" lengthAdjust="spacingAndGlyphs">SERVICE</text>

    <g class="contact-block">
      <text class="contact-line" x="201" y="855">Dale Wexby</text>
      <text class="contact-line" x="201" y="886">4817 Quarry Bend Ave.</text>
      <text class="contact-line" x="201" y="917">#512 San Diego, CA</text>
      <text class="contact-line" x="201" y="947">92417 858-291-6083</text>
      <text class="contact-web" x="201" y="977" textLength="368" lengthAdjust="spacingAndGlyphs">www.glimmertidepoolservice.example</text>
    </g>
  </g>
</svg>
</body>
</html>
```